Business card

creative business card for newly created national firm that specializes in high-density storage for retail markets. Looking for creativity and overall theme that will differentiate from others in this unique niche ...essentially a design that will provide instant recognition as we develop our identity in the marketplace. possible initial thoughts are attached with logo separately

Industry/Entity Type

Retail

```html
<!DOCTYPE html>
<html lang="en">
<head>
<meta charset="utf-8">
<title>Verta Storage Concepts – Business Card</title>
<link rel="stylesheet" href="https://fonts.googleapis.com/css2?family=Lato:wght@300;400;700&display=swap">
<style>
  :root {
    --backdrop: #3a2f24;
    --card: #f7f8f8;
    --band: #4cc3e4;
    --band-deep: #2fa9cf;
    --ink-blue: #41bfe3;
    --ink-teal: #2f7f9c;
    --ink-grey: #4a4f55;
    --white: #ffffff;
  }
  * { box-sizing: border-box; margin: 0; padding: 0; }
  html, body { width: 759px; height: 1200px; overflow: hidden; }
  body {
    background: var(--backdrop);
    font-family: "Lato", sans-serif;
    display: flex;
    flex-direction: column;
    align-items: center;
    justify-content: center;
    gap: 60px;
  }
  .card {
    width: 310px;
    height: 520px;
    background: var(--card);
    border-radius: 16px;
    overflow: hidden;
    position: relative;
    display: flex;
    flex-direction: column;
  }
  /* Front */
  .card--front {
    align-items: center;
    justify-content: center;
    text-align: center;
  }
  .brand {
    display: flex;
    flex-direction: column;
    align-items: center;
    gap: 18px;
  }
  .brand__mark {
    width: 26px;
    height: 26px;
    background: var(--ink-blue);
  }
  .brand__name {
    font-weight: 300;
    font-size: 44px;
    line-height: 1.02;
    letter-spacing: 3px;
    color: var(--ink-teal);
    text-transform: uppercase;
  }
  .brand__tagline {
    font-weight: 700;
    font-size: 13px;
    letter-spacing: 3px;
    color: var(--ink-teal);
    margin-top: 6px;
  }
  /* Back */
  .band {
    background: linear-gradient(180deg, var(--band), var(--band-deep));
    flex: none;
  }
  .band--top { height: 42px; }
  .band--bottom {
    height: 62px;
    display: flex;
    align-items: center;
    justify-content: center;
  }
  .website {
    color: var(--white);
    font-weight: 700;
    font-size: 15px;
    letter-spacing: 0.5px;
  }
  .details {
    flex: 1;
    display: flex;
    flex-direction: column;
    align-items: center;
    text-align: center;
    padding-top: 22px;
    color: var(--ink-blue);
  }
  .person {
    font-size: 25px;
    font-weight: 400;
    letter-spacing: 1px;
    text-transform: uppercase;
  }
  .phone {
    font-size: 21px;
    font-weight: 700;
    letter-spacing: 0.5px;
    color: var(--ink-teal);
    margin-bottom: 26px;
  }
  .contact { margin-bottom: 22px; font-size: 15px; line-height: 1.4; }
  .contact__label {
    display: block;
    font-weight: 700;
    font-size: 16px;
    color: var(--ink-grey);
    text-decoration: underline;
    margin-bottom: 2px;
  }
</style>
</head>
<body>
  <section class="card card--front" aria-label="Card front">
    <div class="brand">
      <span class="brand__mark"></span>
      <h1 class="brand__name">Verta<br>Storage<br>Concepts</h1>
      <p class="brand__tagline">Store Smarter Every Aisle</p>
    </div>
  </section>

  <section class="card card--back" aria-label="Card back">
    <div class="band band--top"></div>
    <div class="details">
      <p class="person">Dorian Halvers</p>
      <p class="phone">844-555-0188</p>
      <p class="contact"><span class="contact__label">Office</span>Juniper Avenue Address<br>Cedar Ridge, AZ 88888</p>
      <p class="contact"><span class="contact__label">E-Mail</span>contact@vertastorage.com</p>
      <p class="contact"><span class="contact__label">Mail</span>PO Box Number<br>Cedar Ridge, AZ 99999</p>
    </div>
    <div class="band band--bottom"><span class="website">www.vertastorage.com</span></div>
  </section>
</body>
</html>
```